Vellorin - Business Cards for a new venture

create business card for a startup classified business dealing in construction materials, the cards need to have a professional look but modern, more serious than playful, one of the samples must include the official font (attached), please explore using the official colors in the company's logo

Target Market(s)

Energy sector

Contact Information for Business Card

Font styles to use
Other font styles liked:
• suissnord

Requirements
Must have
• corporate colors (in logo attached)
Nice to have
• Official font (in one of the samples) font is : suissnord
Should not have
• Cartoonish look

```html
<!DOCTYPE html>
<html lang="en">
<head>
<meta charset="utf-8">
<title>Vellorin – Business Cards</title>
<link href="https://fonts.googleapis.com/css2?family=Yanone+Kaffeesatz:wght@300;400;500&display=swap" rel="stylesheet">
<style>
  :root {
    --stage: #2e3e46;
    --brand-blue: #0b5088;
    --brand-blue-deep: #073b66;
    --brand-grey: #9b9da1;
    --paper: #ffffff;
    --ink: #161616;
    --rule: #c9ced4;
  }
  * { box-sizing: border-box; margin: 0; padding: 0; }
  html, body {
    width: 900px; height: 1200px; overflow: hidden;
    background: var(--stage);
    font-family: "Yanone Kaffeesatz", "Arial Narrow", sans-serif;
  }
  .canvas { position: relative; width: 900px; height: 1200px; }
  .card {
    position: absolute; top: 285px;
    width: 360px; height: 630px;
    overflow: hidden;
    box-shadow: 0 18px 40px rgba(0,0,0,.35);
  }
  .card--front { left: 50px; }
  .card--back { left: 490px; }
  .card__shape { position: absolute; inset: 0; width: 100%; height: 100%; }
  .card__text { position: absolute; left: 0; right: 0; text-align: center; }

  .wordmark {
    display: flex; align-items: center; justify-content: center; gap: 14px;
    color: var(--brand-grey); font-weight: 300;
    font-size: 58px; letter-spacing: 6px; text-transform: uppercase;
  }
  .wordmark__dot {
    width: 16px; height: 16px; border-radius: 50%;
    background: var(--brand-blue);
  }
  .card--front .wordmark { top: 160px; }
  .holder-name { top: 258px; font-size: 38px; font-weight: 500; color: var(--ink); }
  .holder-role {
    top: 305px; font-size: 25px; font-weight: 300; color: var(--ink);
    font-variant: small-caps; letter-spacing: 1px;
  }
  .email {
    top: 488px; font-size: 30px; font-weight: 400; color: var(--rule);
    display: flex; align-items: center; justify-content: center; gap: 18px;
  }
  .email__rule { width: 70px; height: 2px; background: var(--rule); }

  .contact { color: var(--paper); font-weight: 400; line-height: 1.2; }
  .contact--phones { top: 90px; font-size: 29px; }
  .contact--address { top: 178px; font-size: 27px; font-weight: 300; line-height: 1.45; }
  .contact__label { font-weight: 500; }
  .card--back .wordmark { top: 448px; font-size: 50px; }
</style>
</head>
<body>
<main class="canvas">

  <section class="card card--front" aria-label="Business card front">
    <svg class="card__shape" viewBox="0 0 360 630" preserveAspectRatio="none" aria-hidden="true">
      <defs>
        <linearGradient id="frontBlue" x1="0" y1="0" x2="0" y2="1">
          <stop offset="0" stop-color="#0b5088"/>
          <stop offset="1" stop-color="#073b66"/>
        </linearGradient>
      </defs>
      <rect width="360" height="630" fill="url(#frontBlue)"/>
      <path d="M0 40 L360 60 L360 335 L220 365 L180 425 L140 365 L0 335 Z" fill="var(--paper)"/>
    </svg>
    <div class="card__text wordmark"><span class="wordmark__dot"></span>Vellorin</div>
    <p class="card__text holder-name">Name xxxxxxx</p>
    <p class="card__text holder-role">Designer xxxxxxxxx</p>
    <p class="card__text email"><span class="email__rule"></span>email: xxxxxxxxxx<span class="email__rule"></span></p>
  </section>

  <section class="card card--back" aria-label="Business card back">
    <svg class="card__shape" viewBox="0 0 360 630" preserveAspectRatio="none" aria-hidden="true">
      <rect width="360" height="630" fill="var(--paper)"/>
      <path d="M0 0 L360 0 L360 298 L205 298 L180 350 L155 298 L0 298 Z" fill="var(--brand-blue)"/>
      <rect y="592" width="360" height="38" fill="var(--brand-blue)"/>
    </svg>
    <div class="card__text contact contact--phones">
      <p><span class="contact__label">Mobile</span> xxxxxxxxxx</p>
      <p><span class="contact__label">Office:</span> xxxxxxxxxx</p>
    </div>
    <div class="card__text contact contact--address">
      <p><span class="contact__label">Address:</span> xxxx xxxxxx</p>
      <p>xxxx xxxxxx</p>
      <p>xxxx xxxxxx xxx</p>
    </div>
    <div class="card__text wordmark"><span class="wordmark__dot"></span>Vellorin</div>
  </section>

</main>
</body>
</html>
```